Business Card for Lorena Whitfield

Name: Lorena Whitfield
Title: Realtor
Email: Lorena@LorenaWhitfieldRE.com
Phone: 480-555-0137

On the front of the business card, I would like the photo, the contact information and the Lorena Whitfield Logo. The backside is required to have the Broker logo and the required logos. Please use the colors from the logo design. Our company has a classy, professional look.

```html
<!DOCTYPE html>
<html lang="en">
<head>
<meta charset="UTF-8">
<title>Lorena Whitfield – Business Card</title>
<link href="https://fonts.googleapis.com/css2?family=Montserrat:wght@400;500;600&display=swap" rel="stylesheet">
<style>
  :root {
    --backdrop: #e4e4e4;
    --paper: #f4f4f4;
    --brand-red: #b8001f;
    --band-red: #b5001e;
    --ink-grey: #3c3c3c;
    --badge-ink: #1a1a1a;
    --white: #ffffff;
  }
  * { margin: 0; padding: 0; box-sizing: border-box; }
  html, body {
    width: 1200px; height: 900px; overflow: hidden;
    background: var(--backdrop);
    font-family: "Montserrat", sans-serif;
  }
  .canvas { position: relative; width: 1200px; height: 900px; }

  .card {
    position: absolute; left: 270px; width: 660px; height: 377px;
    background: var(--paper); overflow: hidden;
    box-shadow: 0 2px 6px rgba(0,0,0,0.18);
  }
  .card--back { top: 48px; }
  .card--front { top: 473px; }

  /* Back side */
  .back-rule {
    position: absolute; left: 0; right: 0; top: 58px; height: 3px;
    background: var(--brand-red);
  }
  .broker-mark {
    position: absolute; left: 0; right: 0; top: 130px;
    display: flex; align-items: center; justify-content: center; gap: 14px;
  }
  .broker-mark__dot {
    width: 40px; height: 40px; border-radius: 50%;
    border: 2px solid var(--ink-grey);
  }
  .broker-mark__name {
    font-weight: 500; font-size: 22px; letter-spacing: 3px;
    color: var(--ink-grey); text-transform: uppercase;
  }
  .compliance-badges {
    position: absolute; right: 36px; bottom: 34px;
    display: flex; gap: 12px; align-items: center;
  }
  .badge { background: var(--badge-ink); }
  .badge--housing { width: 46px; height: 40px; }
  .badge--member { width: 40px; height: 40px; }
  .badge--listing { width: 66px; height: 30px; }

  /* Front side */
  .front-band {
    position: absolute; left: 0; right: 0; top: 235px; bottom: 0;
    background: var(--band-red);
  }
  .portrait {
    position: absolute; left: 23px; top: 105px;
    width: 200px; height: 200px; border-radius: 50%;
    background: radial-gradient(circle at 50% 45%, #8a8a8a 0%, #5e5e5e 55%, #2e2e2e 100%);
  }
  .agency-mark {
    position: absolute; right: 30px; top: 44px;
    display: flex; align-items: center; gap: 12px;
  }
  .agency-mark__square {
    width: 30px; height: 30px; border: 2px solid var(--brand-red);
  }
  .agency-mark__name {
    font-weight: 600; font-size: 19px; letter-spacing: 1.5px;
    color: var(--brand-red); text-transform: uppercase;
  }
  .agent-name {
    position: absolute; right: 30px; top: 144px;
    font-weight: 500; font-size: 29px; color: var(--brand-red);
  }
  .agent-title {
    position: absolute; right: 30px; top: 186px;
    font-weight: 500; font-size: 19px; color: var(--ink-grey);
  }
  .contact-list {
    position: absolute; right: 30px; top: 268px;
    list-style: none; display: flex; flex-direction: column; gap: 10px;
  }
  .contact-item {
    display: flex; align-items: center; justify-content: flex-end; gap: 12px;
    font-weight: 500; font-size: 19px; color: var(--white);
  }
  .contact-item svg { width: 22px; height: 22px; flex: none; }
</style>
</head>
<body>
<main class="canvas">

  <section class="card card--back" aria-label="Card back">
    <div class="back-rule"></div>
    <div class="broker-mark">
      <span class="broker-mark__dot"></span>
      <span class="broker-mark__name">Halden Crest Realty</span>
    </div>
    <div class="compliance-badges" aria-label="Required compliance badges">
      <span class="badge badge--housing"></span>
      <span class="badge badge--member"></span>
      <span class="badge badge--listing"></span>
    </div>
  </section>

  <section class="card card--front" aria-label="Card front">
    <div class="front-band"></div>
    <div class="portrait" role="img" aria-label="Black and white portrait photo of the agent"></div>

    <div class="agency-mark">
      <span class="agency-mark__square"></span>
      <span class="agency-mark__name">Lorena Whitfield Real Estate</span>
    </div>

    <h1 class="agent-name">Lorena Whitfield</h1>
    <p class="agent-title">Realtor</p>

    <ul class="contact-list">
      <li class="contact-item">
        <span>480-555-0137</span>
        <svg viewBox="0 0 24 24" fill="none" stroke="currentColor" stroke-width="1.6" stroke-linecap="round" stroke-linejoin="round">
          <path d="M22 16.9v3a2 2 0 0 1-2.2 2 19.8 19.8 0 0 1-8.6-3.1 19.5 19.5 0 0 1-6-6A19.8 19.8 0 0 1 2.1 4.2 2 2 0 0 1 4.1 2h3a2 2 0 0 1 2 1.7c.1.9.4 1.8.7 2.7a2 2 0 0 1-.5 2.1L8 9.8a16 16 0 0 0 6 6l1.3-1.3a2 2 0 0 1 2.1-.4c.9.3 1.8.6 2.7.7a2 2 0 0 1 1.7 2z"/>
        </svg>
      </li>
      <li class="contact-item">
        <span>Lorena@LorenaWhitfieldRE.com</span>
        <svg viewBox="0 0 24 24" fill="none" stroke="currentColor" stroke-width="1.6" stroke-linecap="round" stroke-linejoin="round">
          <rect x="2.5" y="4.5" width="19" height="15" rx="3"/>
          <path d="M3 7l9 6 9-6"/>
        </svg>
      </li>
    </ul>
  </section>

</main>
</body>
</html>
```